Company brochure for our unique consulting business

We are a small consulting business offering a unique set of services to our clients.. In simple terms we are a business improvement consultancy helping our clients get the best out of their businesses. We work with clients across multiple sectors and deliver a variety of services. We want to put together a brochure to cover these main themes:1. Who we are2. What we do3. The type of people we employ4. The sectors we work inWhile the brochure needs to have a certain corporate feel to it, we don't want it to be "boring" or "stiff". We would like it to have a slightly "friendly" or "informal" feel to it, to reflect the type of organisation we are.We have a company website http://kellbrookadvisory.example , however we do not want to directly replicate the content or feel as we recognise it needs updating.We would like the brochure to be A4 portrait format. We anticipate requiring 12 sides (including covers) but we are happy to be guided on this based on the content we have provided.The attached ppt file gives the detail of the content to be included and also shows the proposed pagination. For the front cover we would like to try 2 versions, one with the KBA logo and one with the Kellbrook Advisory logo (a file of both is attached)One of the most important pages will be the "Our Services" page. We would like this to cover the centre fold. In the ppt file we have shown an example layout, but this is where we need most help - we are clearly not graphic designers! This page will be the most used page in sales meetings etc.Also attached is the following:1. file for our KellBrook Advisory company logo.2. File for our KBA company logo3. Files for Derek's signatures (for under photos) - Owen's to follow4. Photo of Derek & Owen (person in purple shirt to be cropped out)Thank you and really excited to see what everyone comes back with.Derek & Owen

Target Market(s)

Very broad - Manufacturing, Healthcare, Hospitality

Industry/Entity Type

Management Consulting

Font styles to use
Other font styles liked:
• We use Swiss721, but happy to be guided by designer

Colors
3276b5
85abd2
0355a3
333333
5c5c5c
9d9d9d
d9d9d9

Requirements
Must have
• Corporate feel
Nice to have
• Slightly friendly feel
• Our standard "blue" is (CORRECTION) - R55 G96 B146 #376092 and our standard grey is R197 G178, B179 - #B3B2B2, which we would like to keep, but other colours we are happy to be guided on. Brand guidelines attached.

```html
<!DOCTYPE html>
<html lang="en">
<head>
<meta charset="utf-8">
<title>Our Sectors and Contact Us – Page 10</title>
<link rel="stylesheet" href="https://fonts.googleapis.com/css2?family=Arimo:ital,wght@1,700&family=Roboto:wght@300;400&family=Tinos&display=swap">
<style>
  :root {
    --paper: #ffffff;
    --brand-blue: #376092;
    --brand-grey: #b3b2b2;
    --accent-red: #9b2d2d;
    --ink: #333333;
    --heading-light: #e4e7ec;
    --contact-text: #dde5ef;
  }
  html, body {
    margin: 0;
    padding: 0;
    width: 1200px;
    height: 1200px;
    overflow: hidden;
    background: var(--paper);
  }
  .canvas {
    display: block;
    width: 1200px;
    height: 1200px;
  }
  .section-title {
    font-family: "Arimo", Arial, sans-serif;
    font-style: italic;
    font-weight: 700;
    font-size: 34px;
  }
  .section-title--sectors { fill: var(--accent-red); }
  .section-title--contact { fill: var(--heading-light); }
  .sector-item {
    font-family: "Roboto", Arial, sans-serif;
    font-weight: 400;
    font-size: 11.5px;
    fill: var(--ink);
  }
  .sector-bullet { fill: var(--accent-red); }
  .contact-line {
    font-family: "Roboto", Arial, sans-serif;
    font-weight: 300;
    font-size: 16.5px;
    fill: var(--contact-text);
  }
  .page-number {
    font-family: "Tinos", "Times New Roman", serif;
    font-size: 30px;
    fill: #111111;
  }
  .brand-band { fill: var(--brand-blue); }
  .grey-band { fill: var(--brand-grey); }
</style>
</head>
<body>
<svg class="canvas" viewBox="0 0 1500 1500" xmlns="http://www.w3.org/2000/svg">
  <defs>
    <linearGradient id="leftBackdrop" x1="0" y1="0" x2="0.4" y2="1">
      <stop offset="0" stop-color="#eeeef2"/>
      <stop offset="0.6" stop-color="#dcdde4"/>
      <stop offset="1" stop-color="#8c8fa6"/>
    </linearGradient>
    <linearGradient id="businessPortrait" x1="0" y1="0" x2="1" y2="1">
      <stop offset="0" stop-color="#d6dce4"/>
      <stop offset="0.45" stop-color="#5f7896"/>
      <stop offset="0.75" stop-color="#b98a66"/>
      <stop offset="1" stop-color="#2f4562"/>
    </linearGradient>
    <linearGradient id="railTile" x1="0" y1="0" x2="0" y2="1">
      <stop offset="0" stop-color="#c9587a"/>
      <stop offset="0.35" stop-color="#6b4f8a"/>
      <stop offset="1" stop-color="#2b3a55"/>
    </linearGradient>
    <linearGradient id="healthTile" x1="0" y1="0" x2="1" y2="0">
      <stop offset="0" stop-color="#2f5fa8"/>
      <stop offset="1" stop-color="#3e7fd0"/>
    </linearGradient>
    <linearGradient id="flightTile" x1="0" y1="0" x2="0" y2="1">
      <stop offset="0" stop-color="#2c5a9c"/>
      <stop offset="0.6" stop-color="#4b7ab8"/>
      <stop offset="1" stop-color="#1d2f4e"/>
    </linearGradient>
    <linearGradient id="glassTile" x1="0" y1="0" x2="1" y2="1">
      <stop offset="0" stop-color="#1f6f8c"/>
      <stop offset="0.5" stop-color="#37b4d6"/>
      <stop offset="1" stop-color="#14506a"/>
    </linearGradient>
    <filter id="tileShadow" x="-10%" y="-10%" width="125%" height="130%">
      <feDropShadow dx="3" dy="3" stdDeviation="2.5" flood-color="#000" flood-opacity="0.4"/>
    </filter>
  </defs>

  <g class="spread">
    <rect role="img" aria-label="Soft city skyline and architecture photograph" x="33" y="441" width="1447" height="531" fill="url(#leftBackdrop)"/>
    <polygon role="img" aria-label="Photograph of a businessman in a suit holding a phone, blended with a city skyline" points="1240,441 1480,441 1480,972 1062,972" fill="url(#businessPortrait)"/>

    <polygon class="grey-band" points="420,528 1270,528 1062,972 175,972"/>
    <polygon class="brand-band" points="483,441 1262,441 1055,890 282,890"/>

    <g class="sector-tiles" filter="url(#tileShadow)">
      <rect role="img" aria-label="Rail yard at dusk" x="417" y="482" width="216" height="92" fill="url(#railTile)"/>
      <rect role="img" aria-label="Healthcare worker with stethoscope" x="357" y="603" width="216" height="92" fill="url(#healthTile)"/>
      <rect role="img" aria-label="Aircraft taking off over a runway" x="297" y="723" width="216" height="92" fill="url(#flightTile)"/>
      <rect role="img" aria-label="Modern glass building interior" x="237" y="844" width="216" height="92" fill="url(#glassTile)"/>
    </g>

    <text class="section-title section-title--sectors" x="66" y="508">Our Sectors</text>
    <g class="sector-list">
      <circle class="sector-bullet" cx="135" cy="553" r="2"/><text class="sector-item" x="145" y="557">Health &amp; care</text>
      <circle class="sector-bullet" cx="135" cy="578" r="2"/><text class="sector-item" x="145" y="582">Manufacturing</text>
      <circle class="sector-bullet" cx="135" cy="603" r="2"/><text class="sector-item" x="145" y="607">Hospitality</text>
      <circle class="sector-bullet" cx="135" cy="628" r="2"/><text class="sector-item" x="145" y="632">Infrastructure</text>
      <circle class="sector-bullet" cx="135" cy="653" r="2"/><text class="sector-item" x="145" y="657">Global events</text>
      <circle class="sector-bullet" cx="135" cy="679" r="2"/><text class="sector-item" x="145" y="683">Charities</text>
      <circle class="sector-bullet" cx="135" cy="704" r="2"/><text class="sector-item" x="145" y="708">FMCG</text>
      <circle class="sector-bullet" cx="135" cy="729" r="2"/><text class="sector-item" x="145" y="733">Environment</text>
      <circle class="sector-bullet" cx="135" cy="754" r="2"/><text class="sector-item" x="145" y="758">Retail</text>
      <circle class="sector-bullet" cx="135" cy="779" r="2"/><text class="sector-item" x="145" y="783">Food</text>
      <circle class="sector-bullet" cx="135" cy="804" r="2"/><text class="sector-item" x="145" y="808">Financial</text>
      <circle class="sector-bullet" cx="135" cy="829" r="2"/><text class="sector-item" x="145" y="833">Construction</text>
    </g>

    <text class="section-title section-title--contact" x="780" y="509">Contact us</text>
    <g class="contact-address">
      <text class="contact-line" x="836" y="563">KBA Limited</text>
      <text class="contact-line" x="836" y="587">Millbank House</text>
      <text class="contact-line" x="836" y="610">Canal Row</text>
      <text class="contact-line" x="836" y="634">Northbridge</text>
      <text class="contact-line" x="836" y="657">NB4 7QT</text>
    </g>
    <g class="contact-channels">
      <text class="contact-line" x="836" y="785">Tel: +44 (0) 1632 960418</text>
      <text class="contact-line" x="836" y="809">enquiries@kellbrook.example</text>
      <text class="contact-line" x="836" y="832">www.kellbrook.example</text>
    </g>
  </g>

  <text class="page-number" x="759" y="1045" text-anchor="middle">Page10</text>
</svg>
</body>
</html>
```